Business Card Design needed - Something Awesome!

Need a business card designed. Company is "Harbor Vane Consulting" we do consulting and also have sales automation technology.
I'm going to use thick stock or metal, something really nice... I was thinking about a QR Code on the back that would just upload my contact info to the persons contact, etc -

This is a Strategy Company with a tech feel. I'm open to ideas but really want this to be nice!

I need a template that should include:

Name | Position or Title
D: 555.203.8146
www.harborvaneconsulting.example

I'm going to attach my contact so you can use that one, I need to get this printed.

Target Market(s)

Small to mid size customers, Entrepreneurs etc.

Industry/Entity Type

Consulting, Tech, Private Equity.

Contact Information for Business Card

Name, Phone, Maybe email, URL

Font styles to use
Sans Serif

Colors

Designer to choose only greyscale colors for use in the design.

Requirements
Must have
• Fresh, Clean, stand out from the crowd - will be on thick stock or metal.
Nice to have
• Clean, simple yet impactful.
Should not have
• Not cartoonish

```html
<!DOCTYPE html>
<html lang="en">
<head>
<meta charset="utf-8">
<title>Harbor Vane Consulting – Business Card</title>
<link rel="stylesheet" href="https://fonts.googleapis.com/css2?family=Jost:wght@400;500&display=swap">
<style>
  :root {
    --stage: #2a2a2a;
    --ink: #000000;
    --paper: #ffffff;
    --card-radius: 31px;
  }
  * { margin: 0; padding: 0; box-sizing: border-box; }
  html, body {
    width: 1200px; height: 1200px; overflow: hidden;
    background: var(--stage);
    font-family: "Jost", sans-serif;
  }
  .canvas { position: relative; width: 1200px; height: 1200px; }
  .card {
    position: absolute;
    width: 838px; height: 478px;
    border-radius: var(--card-radius);
    overflow: hidden;
    box-shadow: 0 6px 18px rgba(0,0,0,0.45);
  }
  .card--front { left: 187px; top: 103px; background: var(--ink); }
  .card--back  { left: 195px; top: 619px; background: var(--paper); color: var(--ink); }

  .front-name {
    position: absolute; inset: 0;
    display: flex; align-items: center; justify-content: center;
    color: var(--paper);
    font-weight: 500; font-size: 58px; letter-spacing: 4px;
  }

  .back-shapes { position: absolute; inset: 0; }
  .wordmark {
    position: absolute; left: 64px; top: 76px;
    font-weight: 500; font-size: 80px; line-height: 1; letter-spacing: 2px;
    white-space: nowrap;
  }
  .person { position: absolute; left: 67px; top: 211px; }
  .person__name { font-weight: 400; font-size: 33px; line-height: 1; }
  .person__title { font-weight: 400; font-size: 21px; line-height: 1.2; margin-left: 4px; margin-top: 2px; }

  .contacts { position: absolute; left: 74px; top: 297px; list-style: none; }
  .contacts li {
    display: flex; align-items: center;
    height: 25px; font-size: 20px; line-height: 1;
  }
  .contacts svg { width: 20px; height: 20px; margin-right: 21px; flex: none; }
</style>
</head>
<body>
<div class="canvas">

  <section class="card card--front">
    <div class="front-name">HARBOR VANE</div>
  </section>

  <section class="card card--back">
    <svg class="back-shapes" viewBox="0 0 838 478" width="838" height="478" aria-hidden="true">
      <polygon points="825,0 838,0 838,478 781,478 622,272" fill="var(--ink)"/>
      <polygon points="597,302 733,478 463,478" fill="var(--ink)"/>
    </svg>

    <div class="wordmark">HARBOR VANE</div>

    <div class="person">
      <div class="person__name">Mara Lindqvist, DVM</div>
      <div class="person__title">Director / Doctor</div>
    </div>

    <ul class="contacts">
      <li>
        <svg viewBox="0 0 24 24" aria-hidden="true"><path fill="currentColor" d="M6.6 10.8a15.1 15.1 0 0 0 6.6 6.6l2.2-2.2c.3-.3.7-.4 1-.2 1.1.4 2.3.6 3.6.6.6 0 1 .4 1 1V20c0 .6-.4 1-1 1A17 17 0 0 1 3 4c0-.6.4-1 1-1h3.5c.6 0 1 .4 1 1 0 1.3.2 2.5.6 3.6.1.3 0 .7-.2 1z"/></svg>
        555.203.8146
      </li>
      <li>
        <svg viewBox="0 0 24 24" aria-hidden="true"><g fill="none" stroke="currentColor" stroke-width="2"><circle cx="12" cy="12" r="9"/><path d="M3 12h18M12 3c3 3 3 15 0 18M12 3c-3 3-3 15 0 18"/></g></svg>
        www.harborvaneconsulting.example
      </li>
      <li>
        <svg viewBox="0 0 24 24" aria-hidden="true"><rect x="2" y="5" width="20" height="14" fill="currentColor"/><path d="M2 5l10 8 10-8" fill="none" stroke="#fff" stroke-width="1.6"/></svg>
        mara@harborvaneconsulting.example
      </li>
      <li>
        <svg viewBox="0 0 24 24" aria-hidden="true"><path fill="currentColor" d="M12 2a7 7 0 0 0-7 7c0 5 7 13 7 13s7-8 7-13a7 7 0 0 0-7-7zm0 9.5A2.5 2.5 0 1 1 12 6.5a2.5 2.5 0 0 1 0 5z"/></svg>
        2240 Larkspur Way, Fairhaven, CA 90210
      </li>
    </ul>
  </section>

</div>
</body>
</html>
```